Kestrel Vitality a Centre Pty Ltd

Business card is to promote and represent our new business. It's situated in
47 Fenwick Road
Linden Bay 2104 Sydney
Our clinic is all about getting people back to great health giving them back their lifestyle in half the usual time it takes to get results elsewhere , we do this through innovative therapies with latest state of the art equipment ,skills ,knowledge and experience.
We give them back their pain free healthy lifestyle with lots of energy to love life and perform their best Quickly and effectively .
The final design should communicate
Trust , confidence, results .
Updates

Reason: Waiting for some designers to submit work Thanks

Target Market(s)

High end clients that take their health and results seriously ,
High end athletes , as well as general people that want to see results with different
Treatment Methods and approach

Industry/Entity Type

Clinic

Contact Information for Business Card

Kestrel Vitality Centre Pty Ltd
47 Fenwick Road Linden Bay 2104 Sydney
Website www.kestrelvitalitycentre.com.au

Font styles to use
Other font styles liked:
• Gothic font medium

Requirements
Must have
• A designe that makes people look twice with a wow factor , a designe that isn't like all the rest .
• Must have the logo in the colours Iv provided in my files
• Must communicate Trust, confidence , results
Nice to have
• 1) The logo raised up or
• 2) Maybe a pop up logo on the card ?
• Or let's be creative and have two cards one on top of the other so the two cards slide .... The front will have the kestrel logo with the address details etc
• The other card with have
• eg your next app .......................................repeating all way down the card
Should not have
• Basic plain looking card that everyone else has

```html
<!DOCTYPE html>
<html lang="en">
<head>
<meta charset="utf-8">
<title>Kestrel Vitality Centre — Business Card</title>
<link href="https://fonts.googleapis.com/css2?family=Montserrat:ital,wght@0,400;0,500;0,600;1,400;1,500&display=swap" rel="stylesheet">
<style>
  :root {
    --ink: #06394b;
    --navy: #003849;
    --indigo: #272a6e;
    --sky: #00a6e2;
    --green-dark: #0b6e3a;
    --green-lime: #8cc63f;
    --paper-edge: #e4e4e4;
    --paper-mid: #ffffff;
    --white: #ffffff;
  }
  * { margin: 0; padding: 0; box-sizing: border-box; }
  html, body { width: 1200px; height: 1000px; overflow: hidden; }
  body {
    position: relative;
    font-family: "Montserrat", sans-serif;
    background: radial-gradient(ellipse at 50% 45%, #ffffff 0%, #f3f3f3 45%, #e2e2e2 100%);
  }
  .card {
    position: absolute;
    left: 313px;
    width: 594px;
    height: 342px;
    overflow: hidden;
    box-shadow: 0 4px 12px rgba(0,0,0,0.25);
  }
  .card--front {
    top: 140px;
    background: linear-gradient(90deg, var(--paper-edge) 0%, var(--paper-mid) 50%, var(--paper-edge) 100%);
    color: var(--ink);
  }
  .card--back {
    top: 535px;
    background: var(--navy);
  }
  .brand {
    position: absolute;
    display: flex;
    align-items: center;
    font-weight: 600;
    white-space: nowrap;
  }
  .brand__dot { border-radius: 50%; flex: none; }
  .card--front .brand { left: 24px; top: 26px; gap: 10px; font-size: 20px; color: var(--indigo); }
  .card--front .brand__dot { width: 26px; height: 26px; background: var(--indigo); }
  .card--back .brand { left: 0; right: 0; top: 146px; justify-content: center; gap: 16px; font-size: 32px; color: var(--white); }
  .card--back .brand__dot { width: 44px; height: 44px; background: var(--white); }
  .holder {
    position: absolute;
    left: 0; right: 0; top: 104px;
    text-align: center;
  }
  .holder__name { font-size: 35px; font-weight: 500; letter-spacing: 0.6px; line-height: 1.1; }
  .holder__role { font-size: 20px; font-weight: 400; margin-top: 2px; }
  .contact {
    position: absolute;
    left: 19px; top: 198px;
    font-size: 12px;
    font-style: italic;
    font-weight: 500;
    line-height: 14.5px;
    list-style: none;
  }
  .swoosh { position: absolute; left: 0; top: 0; width: 594px; height: 342px; }
  .web {
    position: absolute;
    left: 0; right: 0; top: 303px;
    text-align: center;
    font-size: 18px;
    font-style: italic;
    color: var(--white);
  }
</style>
</head>
<body>
  <section class="card card--front" aria-label="Business card front">
    <svg class="swoosh" viewBox="0 0 594 342" aria-hidden="true">
      <defs>
        <linearGradient id="bandBlue" x1="0" x2="1">
          <stop offset="0" stop-color="#272a6e"/>
          <stop offset="0.5" stop-color="#00a6e2"/>
          <stop offset="1" stop-color="#272a6e"/>
        </linearGradient>
        <linearGradient id="bandGreen" x1="0" x2="1">
          <stop offset="0" stop-color="#0b6e3a"/>
          <stop offset="0.5" stop-color="#8cc63f"/>
          <stop offset="1" stop-color="#0b6e3a"/>
        </linearGradient>
      </defs>
      <path d="M0,279 Q430,282 594,178 L594,205 Q410,296 0,297 Z" fill="url(#bandBlue)"/>
      <path d="M0,297 Q410,296 594,205 L594,342 L0,342 Z" fill="url(#bandGreen)"/>
    </svg>
    <div class="brand"><span class="brand__dot"></span>Kestrel Vitality Centre</div>
    <div class="holder">
      <h1 class="holder__name">Mara Lindqvist</h1>
      <p class="holder__role">CEO</p>
    </div>
    <ul class="contact">
      <li>47 Fenwick Road Linden Bay 2104 Sydney Website</li>
      <li>Contact no:</li>
      <li>Email:</li>
      <li>Fax:</li>
    </ul>
    <p class="web">www.kestrelvitalitycentre.com.au</p>
  </section>

  <section class="card card--back" aria-label="Business card back">
    <div class="brand"><span class="brand__dot"></span>Kestrel Vitality Centre</div>
  </section>
</body>
</html>
```